Tallbrook Home Exteriors Door Hanger design, Postcard and presentation folders Design

we are a home improvement company in Portland Oregon, are main service is roofing but we also do gutters, painting and pressure washing. we are a certified roofing contractor for QRV. We have over 20years of experince in the roofing industry we use top quality materials. Our mission is to do quality work and provide the best service.

This door hangers are going to be share to homeowners where we are currently working at! I will like to have a square maybe 2 inch wide and 1 inch hide (blank) for me to put the address where we are working at. So we want to give a direct message to homeowners who we are and why we are there for. Our services are roofing, gutters, painting, and pressure washing. But 95% of the door hangers should give the message that we are a roofing contractor. We are also certified by QRV which means all of our new roof projects have a 50 year warranty which only 2% of roofing contractor can offer that. We also offer finance, and all quality work. I will like to add photos of our trucks since all of them are wrap which will build them trust.

Target Market(s)

This door hangers should be custom for Homeowners with residential Homes,,, Average customer are between 40 & 65 Years old.

Industry/Entity Type

Roofing

Contact Information for Business Card

Logo, name, phone number, credentials, and services like roofing gutters painting and pressure washing

Font styles to use
Serif
Sans Serif
Decorative

Colors
33b8a4
5c5c5c

Requirements
Must have
• I want tho have a folder design just like this business card sample i uploaded. Teal and charcoal with services ...
Nice to have
• company trucks, job photo, crew photo and credential photos
Should not have
• I dont want it too busy or crowded..

```html
<!DOCTYPE html>
<html lang="en">
<head>
<meta charset="utf-8">
<title>Tallbrook Home Exteriors – Door Hanger</title>
<link rel="stylesheet" href="https://fonts.googleapis.com/css2?family=Bebas+Neue&family=Libre+Baskerville:wght@400;700&family=Poppins:wght@500;600;700&display=swap">
<style>
  :root {
    --teal: #1f9784;
    --teal-dark: #17705f;
    --lime: #c8d92e;
    --charcoal: #5c5c5c;
    --yellow: #f3e82c;
    --white: #ffffff;
    --rule: #d0d0d0;
  }
  * { box-sizing: border-box; margin: 0; padding: 0; }
  html, body { width: 1200px; height: 1200px; overflow: hidden; background: var(--white); }
  body { position: relative; font-family: "Poppins", sans-serif; }

  .dimension-label { position: absolute; font-family: "Poppins", sans-serif; font-weight: 500; font-size: 19px; color: #222; }
  .dimension-width { left: 352px; top: 44px; }
  .dimension-height { left: 82px; top: 581px; }
  .dimension-line { position: absolute; background: #111; }
  .dimension-line.horizontal { left: 183px; top: 76px; width: 384px; height: 2px; }
  .dimension-line.vertical { left: 138px; top: 98px; width: 2px; height: 1006px; }

  .hanger { position: absolute; top: 98px; width: 388px; height: 1004px; overflow: hidden; background: var(--white); box-shadow: 0 1px 4px rgba(0,0,0,0.12); }
  .hanger-front { left: 182px; }
  .hanger-back { left: 622px; }
  .hanger svg.layer { position: absolute; left: 0; top: 0; }

  .photo { position: absolute; }
  .door-hole { position: absolute; left: 114px; top: 38px; width: 160px; height: 160px; border-radius: 50%; background: var(--white); }
  .door-slit { position: absolute; top: 107px; height: 21px; background: var(--white); }

  /* front */
  .brand-block { position: absolute; left: 0; top: 232px; width: 388px; height: 184px; text-align: center; }
  .brand-mark { position: absolute; left: 168px; top: 26px; width: 52px; height: 52px; background: var(--teal); }
  .brand-name { position: absolute; left: 0; width: 100%; top: 96px; font-family: "Libre Baskerville", serif; font-weight: 700; color: var(--teal); font-size: 19px; line-height: 1.25; }
  .brand-tagline { position: absolute; left: 0; width: 100%; top: 154px; font-family: "Libre Baskerville", serif; font-size: 11px; letter-spacing: 1.5px; color: var(--charcoal); }
  .brand-rule { position: absolute; left: 0; top: 416px; width: 388px; height: 6px; background: var(--lime); }
  .credentials { position: absolute; left: 0; top: 422px; width: 388px; height: 66px; display: flex; align-items: center; justify-content: space-around; padding: 0 18px; }
  .credential { background: #e4e4e4; border: 2px solid var(--charcoal); }
  .credential.round { width: 36px; height: 36px; border-radius: 50%; }
  .credential.shield { width: 50px; height: 48px; border-radius: 8px 8px 22px 22px; background: var(--teal); border-color: var(--teal-dark); }
  .credential.plate { width: 64px; height: 24px; border-radius: 3px; }
  .credential.plate.dark { background: #222; border-color: #222; }
  .credential.plate.red { background: #d8312b; border-color: #d8312b; width: 70px; }
  .message-panel { position: absolute; left: 0; top: 488px; width: 388px; height: 516px; background: var(--teal); }
  .message-headline { position: absolute; left: 0; width: 100%; top: 48px; text-align: center; font-family: "Bebas Neue", sans-serif; color: var(--white); font-size: 32px; line-height: 30px; letter-spacing: 0.3px; }
  .message-sub { position: absolute; left: 0; width: 100%; top: 157px; text-align: center; font-weight: 600; font-size: 12.5px; color: var(--yellow); }
  .message-rule { position: absolute; left: 116px; top: 188px; width: 155px; height: 1px; background: rgba(255,255,255,0.7); }
  .social-row { position: absolute; left: 0; width: 100%; top: 206px; display: flex; justify-content: center; gap: 40px; }
  .social-dot { width: 26px; height: 26px; border: 2px solid var(--white); border-radius: 50%; }
  .address-box { position: absolute; left: 38px; top: 830px; width: 310px; height: 104px; background: var(--white); border-radius: 6px; }
  .address-line { position: absolute; left: 16px; width: 276px; height: 1px; background: var(--rule); }

  /* back */
  .website-band { position: absolute; left: 0; top: 232px; width: 388px; height: 46px; text-align: center; font-weight: 700; color: var(--teal); font-size: 24px; line-height: 46px; letter-spacing: 0.2px; }
  .services-panel { position: absolute; left: 0; top: 290px; width: 388px; height: 184px; background: var(--lime); }
  .services-title { position: absolute; left: 0; width: 100%; top: 16px; text-align: center; font-family: "Bebas Neue", sans-serif; font-size: 34px; color: var(--teal); letter-spacing: 0.5px; }
  .service { position: absolute; display: flex; align-items: center; gap: 7px; font-weight: 600; color: var(--teal); font-size: 12.5px; white-space: nowrap; }
  .service.primary { font-size: 16px; font-weight: 700; }
  .service svg { flex: none; }
  .contact-panel { position: absolute; left: 0; top: 484px; width: 388px; height: 200px; background: var(--teal); }
  .contact-icon { position: absolute; }
  .contact-text { position: absolute; left: 116px; color: var(--white); font-weight: 600; font-size: 14.5px; line-height: 18px; }
  .contact-phone { position: absolute; left: 116px; top: 118px; font-family: "Bebas Neue", sans-serif; color: var(--yellow); font-size: 48px; line-height: 48px; letter-spacing: 0.5px; }
  .gallery { position: absolute; left: 0; top: 688px; width: 388px; height: 316px; display: grid; grid-template-columns: 194px 194px; grid-template-rows: 158px 158px; }
</style>
</head>
<body>

  <div class="dimension-label dimension-width">4,25 in</div>
  <div class="dimension-line horizontal"></div>
  <div class="dimension-label dimension-height">11 in</div>
  <div class="dimension-line vertical"></div>

  <!-- Front of door hanger -->
  <section class="hanger hanger-front">
    <div class="photo" role="img" aria-label="Close-up of teal-toned asphalt roof shingles" style="left:0;top:0;width:388px;height:224px;background:linear-gradient(160deg,#2a8f80 0%,#1c6f63 45%,#2c9a8a 70%,#175e54 100%);"></div>
    <div class="door-slit" style="left:0;width:150px;"></div>
    <div class="door-hole"></div>
    <svg class="layer" width="388" height="236" viewBox="0 0 388 236">
      <path d="M0 216 Q100 222 200 218 T388 214 L388 232 L0 232 Z" fill="#c8d92e"/>
    </svg>

    <div class="brand-block">
      <div class="brand-mark"></div>
      <div class="brand-name">TALLBROOK HOME EXTERIORS</div>
      <div class="brand-tagline">WHEN QUALITY MATTERS</div>
    </div>
    <div class="brand-rule"></div>

    <div class="credentials">
      <div class="credential round"></div>
      <div class="credential shield"></div>
      <div class="credential plate dark"></div>
      <div class="credential round"></div>
      <div class="credential plate red"></div>
    </div>

    <div class="message-panel">
      <div class="message-headline">We are working in your<br>neighborhood, you can<br>find us here.</div>
      <div class="message-sub">Let Our Experts Help With Your Next Home Project.</div>
      <div class="message-rule"></div>
      <div class="social-row">
        <div class="social-dot"></div>
        <div class="social-dot"></div>
        <div class="social-dot"></div>
      </div>
    </div>

    <svg class="layer" width="388" height="1004" viewBox="0 0 388 1004" role="img" aria-label="Photo of a beige-sided house with grey shingle roof">
      <defs>
        <linearGradient id="houseTone" x1="0" y1="0" x2="1" y2="1">
          <stop offset="0" stop-color="#8a8a86"/>
          <stop offset="0.5" stop-color="#5e6062"/>
          <stop offset="1" stop-color="#b7ac8e"/>
        </linearGradient>
      </defs>
      <polygon points="0,724 26,700 190,778 300,736 388,720 388,1004 0,1004" fill="url(#houseTone)"/>
    </svg>

    <div class="address-box">
      <div class="address-line" style="top:36px;"></div>
      <div class="address-line" style="top:72px;"></div>
    </div>
  </section>

  <!-- Back of door hanger -->
  <section class="hanger hanger-back">
    <div class="photo" role="img" aria-label="Teal-tinted photo of a two-storey home exterior" style="left:0;top:0;width:388px;height:224px;background:linear-gradient(180deg,#2a9a88 0%,#1f7d6f 50%,#155a50 100%);"></div>
    <div class="door-slit" style="left:240px;width:148px;"></div>
    <div class="door-hole"></div>
    <svg class="layer" width="388" height="300" viewBox="0 0 388 300">
      <path d="M0 216 Q100 222 200 218 T388 214 L388 232 L0 232 Z" fill="#c8d92e"/>
      <path d="M0 276 Q120 280 220 277 T388 274 L388 292 L0 292 Z" fill="#1f9784"/>
    </svg>

    <div class="website-band">tallbrookexteriors.com</div>

    <div class="services-panel">
      <div class="services-title">Our Services.</div>
      <div class="service primary" style="left:45px;top:68px;"><svg width="18" height="16" viewBox="0 0 18 16"><path d="M2 9 L7 14 L16 2" fill="none" stroke="#1f9784" stroke-width="3.4" stroke-linecap="round"/></svg>ROOFING</div>
      <div class="service" style="left:190px;top:70px;"><svg width="18" height="16" viewBox="0 0 18 16"><path d="M2 9 L7 14 L16 2" fill="none" stroke="#1f9784" stroke-width="3.4" stroke-linecap="round"/></svg>SIDING</div>
      <div class="service" style="left:45px;top:106px;"><svg width="18" height="16" viewBox="0 0 18 16"><path d="M2 9 L7 14 L16 2" fill="none" stroke="#1f9784" stroke-width="3.4" stroke-linecap="round"/></svg>GUTTERS</div>
      <div class="service" style="left:190px;top:106px;"><svg width="18" height="16" viewBox="0 0 18 16"><path d="M2 9 L7 14 L16 2" fill="none" stroke="#1f9784" stroke-width="3.4" stroke-linecap="round"/></svg>PRESSURE WASHING</div>
      <div class="service" style="left:45px;top:142px;"><svg width="18" height="16" viewBox="0 0 18 16"><path d="M2 9 L7 14 L16 2" fill="none" stroke="#1f9784" stroke-width="3.4" stroke-linecap="round"/></svg>PAINTING</div>
      <div class="service" style="left:190px;top:142px;"><svg width="18" height="16" viewBox="0 0 18 16"><path d="M2 9 L7 14 L16 2" fill="none" stroke="#1f9784" stroke-width="3.4" stroke-linecap="round"/></svg>ATTIC VENTILATON</div>
    </div>

    <div class="contact-panel">
      <svg class="contact-icon" style="left:64px;top:22px;" width="30" height="18" viewBox="0 0 30 18"><path d="M0 0 H23 L30 9 L23 18 H0 Z" fill="#8e8e8e"/><path d="M13 14 C9 9 9 8 9 7 A4 4 0 0 1 17 7 C17 8 17 9 13 14 Z" fill="none" stroke="#fff" stroke-width="1.2"/><circle cx="13" cy="7" r="1.3" fill="#fff"/></svg>
      <div class="contact-text" style="top:22px;">Portland,<br>OR 97000,<br>United States</div>
      <svg class="contact-icon" style="left:64px;top:86px;" width="30" height="18" viewBox="0 0 30 18"><path d="M0 0 H23 L30 9 L23 18 H0 Z" fill="#8e8e8e"/><rect x="8" y="5" width="11" height="8" fill="none" stroke="#fff" stroke-width="1.2"/><path d="M8 5 L13.5 10 L19 5" fill="none" stroke="#fff" stroke-width="1.2"/></svg>
      <div class="contact-text" style="top:85px;">info@tallbrookexteriors.com</div>
      <svg class="contact-icon" style="left:38px;top:127px;" width="54" height="31" viewBox="0 0 54 31"><path d="M0 0 H42 L54 15.5 L42 31 H0 Z" fill="#8e8e8e"/><path d="M24 8 C20 10 20 21 24 23 L27 20 L25 17 L24 17 C23 15 23 13 24 12 L25 12 L27 10 Z" fill="#fff"/></svg>
      <div class="contact-phone">(503)555-0148</div>
    </div>
    <svg class="layer" width="388" height="700" viewBox="0 0 388 700">
      <path d="M0 680 Q120 676 220 680 T388 678 L388 690 L0 690 Z" fill="#c8d92e"/>
    </svg>

    <div class="gallery">
      <div role="img" aria-label="Crew member pressure washing a driveway" style="background:linear-gradient(135deg,#8c8478,#6d675e 60%,#9a9388);"></div>
      <div role="img" aria-label="Crew member in branded shirt washing a window" style="background:linear-gradient(160deg,#c9c3b6,#7c7466 55%,#3a3a3a);"></div>
      <div role="img" aria-label="Crew member spray painting house siding" style="background:linear-gradient(120deg,#cfc6a8,#b3aa8c 50%,#2f3133);"></div>
      <div role="img" aria-label="Company-wrapped pickup truck" style="background:linear-gradient(150deg,#9aa3a8,#6e9aa8 50%,#3a4a52);"></div>
    </div>
  </section>

</body>
</html>
```